Real Estate Website

Please design a real estate website

The menu needs to be :
Home
About us
Houses for sale
Land for sale
Sold properties
Holiday accommodation
Rentals
Consumer affairs
Contact us.

Contact details to show in the footer:
Pinecrest Real Estate
27 Hollowmere Drive
Golden Beach 3851
03 5290 7741

Please add a 'contact us' form in the footer like on https://www.quillbrookestate.com.au/

Design of site should be a photo/slideshow please make it a lifestyle shot and use a photo from a google image search of 'golden beach victoria australia' as a placeholder.

Under this needs to be a section for a heading and description with about us button.

Further under this should be 6 feature properties like https://www.marlowvaleproperty.com.au/ and then under that a 'book a free appraisal' banner like the one on https://www.marlowvaleproperty.com.au/

Attached is the business logo

```html
<!DOCTYPE html>
<html lang="en">
<head>
<meta charset="utf-8">
<title>Pinecrest Real Estate — Golden Beach Victoria</title>
<link href="https://fonts.googleapis.com/css2?family=Poppins:wght@400;500;600;700&display=swap" rel="stylesheet">
<style>
:root{
  --blue:#1c4f9c;
  --blue-dark:#163f7e;
  --gold:#c4a46b;
  --cream:#fbf6ec;
  --ink:#1f2430;
  --muted:#6d7380;
  --line:#dfe3ea;
  --white:#ffffff;
  --stage:#f2f3f6;
}
*{box-sizing:border-box;margin:0;padding:0}
html,body{width:1200px;height:3124px;overflow:hidden}
body{background:var(--stage);font-family:"Poppins",sans-serif;color:var(--ink);position:relative}
.stage-band{position:absolute;left:0;top:350px;width:1200px;height:910px;background:var(--blue)}
.page{position:absolute;left:232px;top:112px;width:792px;height:2910px;background:var(--white);overflow:hidden;box-shadow:0 6px 30px rgba(0,0,0,.15)}
p{font-size:9px;line-height:1.6;color:var(--muted)}
.btn{display:inline-block;background:var(--gold);color:var(--white);font-size:8px;font-weight:500;padding:6px 14px;border-radius:2px}
.section-title{font-size:17px;font-weight:600;text-align:center}

/* header */
.site-header{height:56px;padding:0 28px;display:flex;align-items:center;justify-content:space-between;border-bottom:3px solid var(--gold)}
.brand{display:flex;align-items:center;gap:6px}
.brand-mark{width:14px;height:14px;background:var(--blue)}
.brand-name{font-size:10px;font-weight:600;color:var(--blue)}
.nav-wrap{display:flex;flex-direction:column;align-items:flex-end;gap:6px}
.nav-top,.nav-main{display:flex;gap:16px;font-size:7px;color:var(--ink);align-items:center}
.nav-main{background:var(--gold);padding:4px 12px;color:var(--white)}
.social{display:flex;gap:4px}
.social span{width:11px;height:11px;border-radius:50%;background:var(--blue)}

/* hero */
.hero{height:332px;position:relative;background:linear-gradient(180deg,#6d8fae 0%,#8ea7bb 35%,#7a6a52 60%,#3f4d5a 100%);text-align:center;color:var(--white)}
.hero h1{position:absolute;top:112px;left:0;right:0;font-size:26px;font-weight:600;line-height:1.35}
.hero .btn{position:absolute;top:200px;left:50%;transform:translateX(-50%)}

/* about */
.about{position:relative;height:340px}
.about-frame{position:absolute;left:140px;top:54px;width:60px;height:160px;background:var(--gold)}
.about-photo{position:absolute;left:156px;top:84px;width:210px;height:130px;background:linear-gradient(135deg,#dbe6ee,#9cb7c9)}
.about-text{position:absolute;left:460px;top:80px;width:210px}
.about-text h2{font-size:15px;font-weight:600;margin-bottom:8px}
.about-text .btn{margin-top:12px}

/* stats */
.stats{height:100px;display:flex;justify-content:center;gap:80px;padding-top:0}
.stat{width:90px}
.stat svg{display:block;margin-bottom:6px}
.stat b{font-size:15px;font-weight:600;display:block}
.stat small{font-size:7px;color:var(--muted)}

/* features */
.features{margin-top:50px;height:470px;background:var(--cream);padding-top:26px}
.feature-grid{width:600px;margin:24px auto 0;display:grid;grid-template-columns:repeat(3,1fr);gap:14px 12px}
.card{height:160px;position:relative;color:var(--white);overflow:hidden}
.card .photo{position:absolute;inset:0}
.card .info{position:absolute;left:0;right:0;bottom:0;padding:8px 10px;background:linear-gradient(transparent,rgba(0,0,0,.65))}
.card .price{display:inline-block;background:var(--gold);font-size:7px;padding:2px 6px;margin-bottom:4px}
.card h3{font-size:9px;font-weight:600}
.card small{font-size:7px;opacity:.9}

/* appraisal banner */
.appraisal{position:relative;margin-top:60px;height:200px;background:var(--blue);color:var(--white)}
.appraisal-text{position:absolute;left:40px;top:36px;width:290px}
.appraisal-text h2{font-size:15px;font-weight:600;line-height:1.35;margin-bottom:8px}
.appraisal-text p{color:#dbe4f2}
.appraisal-text .btn{margin-top:12px}
.appraisal-photo{position:absolute;right:0;top:0;width:440px;height:200px;background:linear-gradient(180deg,#cfe0f1,#7f97b3 60%,#4d6079);clip-path:polygon(20% 0,100% 0,100% 100%,0 100%)}

/* houses & land */
.listing{position:relative;height:240px}
.houses{margin-top:40px}
.houses .frame{position:absolute;left:130px;top:20px;width:60px;height:170px;background:var(--blue)}
.houses .photo{position:absolute;left:150px;top:40px;width:180px;height:160px;background:linear-gradient(135deg,#a9aeb5,#6b6f75)}
.houses .text{position:absolute;left:460px;top:70px;width:200px}
.land{height:260px}
.land .text{position:absolute;left:140px;top:50px;width:200px}
.land .frame{position:absolute;left:620px;top:90px;width:30px;height:130px;background:var(--gold)}
.land .photo{position:absolute;left:430px;top:20px;width:210px;height:170px;background:linear-gradient(135deg,#e3e6ea,#a7b3bf)}
.listing h2{font-size:14px;font-weight:600;margin-bottom:8px}
.listing .btn{margin-top:12px}

/* testimonials */
.testimonials{height:320px;padding-top:20px}
.quote-grid{width:600px;margin:26px auto 0;display:grid;grid-template-columns:repeat(3,1fr);gap:16px}
.quote{background:var(--white);box-shadow:0 3px 14px rgba(0,0,0,.1);padding:16px 14px 0;height:200px;text-align:center;position:relative;border-bottom:4px solid var(--blue)}
.quote p{text-align:left}
.quote b{display:block;font-size:8px;margin-top:10px}
.quote small{font-size:7px;color:var(--muted)}
.avatar{width:34px;height:34px;border-radius:50%;background:linear-gradient(135deg,#c9b39a,#6d5a4a);margin:10px auto 0}

/* contact */
.contact{height:270px;padding-top:10px}
.contact-form{width:480px;margin:20px auto 0;display:grid;grid-template-columns:repeat(3,1fr);gap:8px}
.field{border:1px solid var(--line);height:24px;font-size:7px;color:var(--muted);padding:7px 8px}
.field.wide{grid-column:1/4;height:80px}
.contact .btn{display:block;width:80px;margin:16px auto 0;text-align:center}

/* footer */
.site-footer{position:absolute;left:0;bottom:0;width:792px;height:172px;background:var(--blue);color:var(--white)}
.footer-badge{position:absolute;left:50px;top:0;width:120px;height:130px;background:var(--white);clip-path:polygon(0 0,100% 0,50% 100%)}
.footer-badge span{position:absolute;top:28px;left:0;right:0;text-align:center;font-size:8px;font-weight:600;color:var(--blue);line-height:1.3}
.footer-links{position:absolute;left:220px;top:24px;display:flex;gap:32px;font-size:7px}
.footer-contact{position:absolute;left:220px;top:70px;display:flex;gap:60px;font-size:7px;line-height:1.7;color:#dbe4f2}
.footer-bottom{position:absolute;left:220px;right:40px;bottom:22px;display:flex;justify-content:space-between;font-size:6.5px;color:#c5d2e8}
.footer-bottom .social span{background:var(--white);width:9px;height:9px}
</style>
</head>
<body>
<div class="stage-band"></div>
<main class="page">
  <header class="site-header">
    <div class="brand"><span class="brand-mark"></span><span class="brand-name">Pinecrest Real Estate</span></div>
    <div class="nav-wrap">
      <nav class="nav-top"><span>Sold properties</span><span>Holiday accommodation</span><span>Rentals</span>
        <span class="social"><span></span><span></span><span></span></span></nav>
      <nav class="nav-main"><span>Home</span><span>About us</span><span>Houses for sale</span><span>Land for sale</span><span>Consumer affairs</span><span>Contact us</span></nav>
    </div>
  </header>

  <section class="hero" role="img" aria-label="Lifestyle photo of the coastline at Golden Beach, Victoria">
    <h1>Golden Beach Victoria<br>Australia</h1>
    <span class="btn">Read More</span>
  </section>

  <section class="about">
    <div class="about-frame"></div>
    <div class="about-photo" role="img" aria-label="Hands holding a small model house"></div>
    <div class="about-text">
      <h2>About Us</h2>
      <p>We are a local agency helping families buy, sell and rent along the coast. Our team knows every street in town and works hard to give honest advice, fair prices and a simple, friendly experience from first call to handing over the keys.</p>
      <span class="btn">About Us</span>
    </div>
  </section>

  <section class="stats">
    <div class="stat"><svg width="18" height="18" viewBox="0 0 18 18" fill="none" stroke="#1f2430" stroke-width="1.4"><path d="M2 16V8l7-6 7 6v8H2z"/></svg><b>560+</b><small>Homes sold</small></div>
    <div class="stat"><svg width="18" height="18" viewBox="0 0 18 18" fill="none" stroke="#1f2430" stroke-width="1.4"><rect x="3" y="2" width="12" height="14"/><path d="M6 6h2M10 6h2M6 10h2M10 10h2"/></svg><b>197+</b><small>Apartments listed</small></div>
    <div class="stat"><svg width="18" height="18" viewBox="0 0 18 18" fill="none" stroke="#1f2430" stroke-width="1.4"><path d="M2 16h14M4 16V7h10v9M9 2v5"/></svg><b>268+</b><small>Happy clients</small></div>
    <div class="stat"><svg width="18" height="18" viewBox="0 0 18 18" fill="none" stroke="#1f2430" stroke-width="1.4"><circle cx="9" cy="8" r="5"/><path d="M9 13v4"/></svg><b>340+</b><small>Land parcels</small></div>
  </section>

  <section class="features">
    <h2 class="section-title">Feature properties</h2>
    <div class="feature-grid">
      <article class="card"><div class="photo" role="img" aria-label="Modern house exterior" style="background:linear-gradient(160deg,#9fc0dc,#6c7e63)"></div><div class="info"><span class="price">$450,000</span><h3>Coastal Family Home</h3><small>12 Shore Road, Golden Beach</small></div></article>
      <article class="card"><div class="photo" role="img" aria-label="Two storey house exterior" style="background:linear-gradient(160deg,#b7c7d6,#5d6167)"></div><div class="info"><span class="price">$520,000</span><h3>Modern Beach House</h3><small>8 Dune Street, Golden Beach</small></div></article>
      <article class="card"><div class="photo" role="img" aria-label="Brick house with garden" style="background:linear-gradient(160deg,#a6bfd4,#6f5f50)"></div><div class="info"><span class="price">$395,000</span><h3>Cosy Brick Cottage</h3><small>3 Lagoon Court, Golden Beach</small></div></article>
      <article class="card"><div class="photo" role="img" aria-label="Suburban house at dusk" style="background:linear-gradient(160deg,#8ea4b8,#4d4c4a)"></div><div class="info"><span class="price">$610,000</span><h3>Spacious Home For Sale</h3><small>21 Ocean View, Golden Beach</small></div></article>
      <article class="card"><div class="photo" role="img" aria-label="House with lawn" style="background:linear-gradient(160deg,#bcd0e0,#6a7560)"></div><div class="info"><span class="price">$480,000</span><h3>Home In Quiet Street</h3><small>5 Heath Lane, Golden Beach</small></div></article>
      <article class="card"><div class="photo" role="img" aria-label="Large family house" style="background:linear-gradient(160deg,#a9b9c6,#5e5a55)"></div><div class="info"><span class="price">$575,000</span><h3>Luxury Family Home</h3><small>17 Banksia Ave, Golden Beach</small></div></article>
    </div>
  </section>

  <section class="appraisal">
    <div class="appraisal-text">
      <h2>Sell your Property with Marlowvale Property</h2>
      <p>Thinking of selling? Book a free appraisal with our local team and find out what your home is worth in today's market, with no cost and no obligation.</p>
      <span class="btn">Book a Free Appraisal</span>
    </div>
    <div class="appraisal-photo" role="img" aria-label="City skyline of tall buildings"></div>
  </section>

  <section class="listing houses">
    <div class="frame"></div>
    <div class="photo" role="img" aria-label="Agent holding a small house model"></div>
    <div class="text">
      <h2>Houses for sale</h2>
      <p>Browse our full range of homes for sale, from beachside cottages to large family houses, all with clear details and photos.</p>
      <span class="btn">Read More</span>
    </div>
  </section>

  <section class="listing land">
    <div class="text">
      <h2>Land for sale</h2>
      <p>Find vacant blocks and acreage ready to build your dream home, close to the beach, shops and local schools.</p>
      <span class="btn">Read More</span>
    </div>
    <div class="frame"></div>
    <div class="photo" role="img" aria-label="Hand holding a for sale sign"></div>
  </section>

  <section class="testimonials">
    <h2 class="section-title">Client Are Saying</h2>
    <div class="quote-grid">
      <div class="quote"><p>The team made selling our home easy. They kept us informed at every step and got a great result.</p><b>Mr. Ryan Smith</b><small>Golden Beach</small><div class="avatar" role="img" aria-label="Client portrait"></div></div>
      <div class="quote"><p>Friendly, honest and local. We found our holiday house quickly and the process was smooth.</p><b>Mr. Owen Hale</b><small>Sale</small><div class="avatar" role="img" aria-label="Client portrait"></div></div>
      <div class="quote"><p>Great advice on our block of land. We would happily recommend this agency to anyone.</p><b>Mr. Dean Carter</b><small>Paradise Beach</small><div class="avatar" role="img" aria-label="Client portrait"></div></div>
    </div>
  </section>

  <section class="contact">
    <h2 class="section-title">Client Are Saying</h2>
    <form class="contact-form">
      <div class="field">First Name</div><div class="field">Last Name</div><div class="field">Phone Number</div>
      <div class="field wide">Message</div>
    </form>
    <span class="btn">Send Now</span>
  </section>

  <footer class="site-footer">
    <div class="footer-badge"><span>Pinecrest<br>Real Estate</span></div>
    <nav class="footer-links"><span>Home</span><span>About us</span><span>Rentals</span><span>Consumer affairs</span><span>Holiday Accom</span><span>Contact us</span></nav>
    <div class="footer-contact">
      <div>27 Hollowmere Drive<br>Golden Beach 3851</div>
      <div>Phone<br>03 5290 7741</div>
      <div>Email<br>info@pinecrest.com.au</div>
    </div>
    <div class="footer-bottom"><span>© 2024 Pinecrest Real Estate · Privacy Policy · Site map</span><span class="social"><span></span><span></span><span></span></span></div>
  </footer>
</main>
</body>
</html>
```